Kelvane Plumbing Business cards

Company is Kelvane Plumbing.
name Dashel Morrowby, I am a plumber, drainer, gasfitter and roofer
Mobile: 0431 906 154
Email address: info@kelvaneplumbing.example (check out my website for some ideas)
Website: www.kelvaneplumbing.example
ABN: 82 916 203 471
LIC: 604517K

I am reliable all round plumber. I am a 24 hour emergency service. Kelvane Plumbing is a professional plumbing service in the Illawarra, South Coast, Southern Sydney and Southern Highland regions of NSW. We offer a 24 hour emergency service for piece of mind to our customers. Call us now to see how we can help you. Kelvane Plumbing approaches every job with attention to detail and excellent customer service. With our superior workmanship you can be confident that the job will be done right the first time around. You can rest assured with results that are guaranteed to last.

Target Market(s)

the general public

Contact Information for Business Card

look up website for some ideas something with similar colours to logo and new modern and to catch the eye.

Colors
fdfdfd
ffffff
000000
7f7f7f
aaaaaa
33a6d7
0492cd

Requirements
Must have
• all contact details
• company- Kelvane Plumbing
• name- Dashel Morrowby
• number mobile- 0431 906 154
• Email address- info@kelvaneplumbing.example
• Website- www.kelvaneplumbing.example
• ABN- 82 916 203 471
• LIC- 604517K

```html
<!DOCTYPE html>
<html lang="en">
<head>
<meta charset="utf-8">
<title>Kelvane Plumbing – Business Cards</title>
<link rel="stylesheet" href="https://fonts.googleapis.com/css2?family=Open+Sans:wght@400;600;700&display=swap">
<style>
  :root {
    --page-bg: #ffffff;
    --card-base: #1f1d1e;
    --card-glow: #3a3839;
    --brand-blue: #1ba8d6;
    --text-white: #fdfdfd;
    --text-grey: #aaaaaa;
    --icon-grey: #e6e6e6;
  }
  * { box-sizing: border-box; margin: 0; padding: 0; }
  html, body {
    width: 1200px; height: 1200px; overflow: hidden;
    background: var(--page-bg);
    font-family: "Open Sans", Arial, sans-serif;
  }
  .sheet {
    width: 1200px; height: 1200px;
    display: flex; flex-direction: column; align-items: center; justify-content: center;
    gap: 60px;
  }
  .card {
    position: relative;
    width: 900px; height: 514px;
    border-radius: 24px;
    overflow: hidden;
    background: radial-gradient(circle at 55% 50%, var(--card-glow) 0%, var(--card-base) 55%);
    box-shadow: 0 6px 22px rgba(0,0,0,0.18);
  }

  /* Front */
  .brand-name {
    position: absolute; top: 78px; right: 90px;
    color: var(--brand-blue);
    font-size: 40px; font-weight: 700; letter-spacing: 1px;
  }
  .holder-name {
    position: absolute; left: 100px; top: 222px;
    color: var(--text-white);
    font-size: 34px; font-weight: 600;
  }
  .contact-list {
    position: absolute; left: 100px; top: 290px;
    list-style: none;
    display: flex; flex-direction: column; gap: 8px;
  }
  .contact-item {
    display: flex; align-items: center; gap: 18px;
    color: var(--text-white);
    font-size: 24px; font-weight: 400; line-height: 30px;
  }
  .contact-icon { width: 24px; height: 24px; flex: none; }
  .service-band {
    position: absolute; left: 0; right: 0; bottom: 30px; height: 40px;
    background: var(--brand-blue);
    display: flex; align-items: center; justify-content: center;
    color: var(--text-white);
    font-size: 19px; font-weight: 600; letter-spacing: 2.5px;
  }

  /* Back */
  .card--back .brand-name {
    top: 190px; right: auto; left: 0; width: 100%;
    text-align: center; font-size: 58px;
  }
  .registration {
    position: absolute; left: 0; right: 0; bottom: 70px;
    text-align: center;
    color: var(--text-white);
    font-size: 22px; font-weight: 400;
  }
  .registration strong { font-weight: 700; }
  .registration .divider { color: var(--brand-blue); margin: 0 14px; }
</style>
</head>
<body>
<main class="sheet">

  <section class="card card--front" aria-label="Business card front">
    <div class="brand-name">Kelvane Plumbing</div>
    <h1 class="holder-name">Dashel Morrowby</h1>
    <ul class="contact-list">
      <li class="contact-item">
        <svg class="contact-icon" viewBox="0 0 24 24" fill="none" stroke="currentColor" stroke-width="1.8" aria-hidden="true">
          <rect x="6.5" y="2" width="11" height="20" rx="2"/><line x1="10.5" y1="18.5" x2="13.5" y2="18.5"/>
        </svg>
        0431 906 154
      </li>
      <li class="contact-item">
        <svg class="contact-icon" viewBox="0 0 24 24" fill="currentColor" aria-hidden="true">
          <path d="M2 5h20v14H2z M3.5 6.5 12 13l8.5-6.5" fill="none" stroke="currentColor" stroke-width="1.8"/>
          <path d="M2 5l10 8 10-8v1.5l-10 8-10-8z"/>
        </svg>
        info@kelvaneplumbing.example
      </li>
      <li class="contact-item">
        <svg class="contact-icon" viewBox="0 0 24 24" fill="none" stroke="currentColor" stroke-width="1.6" aria-hidden="true">
          <circle cx="12" cy="12" r="10"/><ellipse cx="12" cy="12" rx="4.5" ry="10"/>
          <line x1="2" y1="12" x2="22" y2="12"/><path d="M4 6.5h16M4 17.5h16"/>
        </svg>
        www.kelvaneplumbing.example
      </li>
    </ul>
    <div class="service-band">PLUMBING, DRAINAGE, GASFITTING &amp; ROOFING</div>
  </section>

  <section class="card card--back" aria-label="Business card back">
    <div class="brand-name">Kelvane Plumbing</div>
    <p class="registration">
      <strong>ABN:</strong> 82 916 203 471<span class="divider">·</span><strong>LIC:</strong> 604517K
    </p>
  </section>

</main>
</body>
</html>
```